VENTURE CAPITAL GROUP BUSINESS CARD DESIGN

Venture Capital Group based in SF looking for a bold business card design. No trendy colour explosion, 3D effects etc. Just "simple" optical effects. Works on your brain, keeps your eye focused and sticks to your mind.
Target Market(s)
Technology startups
Industry/Entity Type
Venture Capital
Contact Information for Business Card
BARTHOLOMEW ELLING
MANAGING PARTNER
817 FERN ST SAN FRANCISCO, CA 94111
415.555.0142 O
415.555.0187 F
415.555.0236 C
bart@quillbrookfunds.example

```html
<!DOCTYPE html>
<html lang="en">
<head>
<meta charset="utf-8">
<title>Quillbrook Funds – Business Card</title>
<link rel="stylesheet" href="https://fonts.googleapis.com/css2?family=Ubuntu:ital,wght@0,400;1,400&family=Arimo:wght@400&display=swap">
<style>
  :root {
    --page: #f4f5f4;
    --card-white: #ffffff;
    --brand-green: #1e8a1a;
    --band-green: #127208;
    --rule-grey: #9eabb0;
    --mark-grey: #e6e8e8;
    --pattern-light: #4fd22e;
    --pattern-dark: #1d9a12;
    --ink-light: #ffffff;
  }
  * { margin: 0; padding: 0; box-sizing: border-box; }
  html, body {
    width: 995px; height: 1200px; overflow: hidden;
    background: var(--page);
  }
  .sheet { position: relative; width: 995px; height: 1200px; }

  /* Front of card */
  .card-front {
    position: absolute; left: 51px; top: 50px;
    width: 888px; height: 521px;
    background: var(--card-white);
    overflow: hidden;
  }
  .brand {
    position: absolute; left: 0; right: 0; top: 34px;
    display: flex; flex-direction: column; align-items: center;
  }
  .brand-dot {
    width: 172px; height: 172px; border-radius: 50%;
    background: radial-gradient(circle at 40% 40%, #ffffff, var(--mark-grey));
  }
  .brand-name {
    margin-top: 20px;
    font-family: "Ubuntu", sans-serif; font-weight: 400;
    font-size: 40px; line-height: 46px; letter-spacing: 1px;
    color: var(--brand-green);
    white-space: nowrap;
  }
  .holder {
    position: absolute; left: 0; right: 0; top: 294px;
    text-align: center;
    font-family: "Ubuntu", sans-serif;
    color: var(--brand-green);
  }
  .holder-name { font-size: 21px; line-height: 24px; }
  .holder-title { font-size: 19px; font-style: italic; line-height: 23px; }

  .rule-grey {
    position: absolute; left: 0; right: 0; top: 355px; height: 13px;
    background: var(--rule-grey);
  }
  .contact-band {
    position: absolute; left: 0; right: 0; top: 371px; bottom: 0;
    background: var(--band-green);
    font-family: "Arimo", sans-serif; color: var(--ink-light);
  }
  .contact-left {
    position: absolute; left: 47px; top: 16px;
    font-size: 22px; line-height: 24.5px; letter-spacing: 0.6px;
  }
  .contact-right {
    position: absolute; right: 42px; top: 77px;
    text-align: right; font-size: 21px; line-height: 24.5px;
  }

  /* Back of card */
  .card-back {
    position: absolute; left: 47px; top: 604px;
    width: 895px; height: 526px;
    border: 5px solid var(--card-white);
    overflow: hidden;
  }
  .back-pattern {
    position: absolute; inset: 0;
    background: radial-gradient(circle at 50% 40%, var(--pattern-light), var(--pattern-dark));
  }
  .back-brand {
    position: absolute; left: 0; right: 0; top: 56px;
    display: flex; flex-direction: column; align-items: center;
  }
  .back-brand .brand-dot {
    width: 200px; height: 200px;
    background: rgba(255,255,255,0.28);
  }
  .back-brand .brand-name {
    color: var(--ink-light);
    margin-top: 16px;
    opacity: 0.85;
  }
  .back-band {
    position: absolute; left: 0; right: 0; top: 356px; height: 104px;
    background: rgba(10, 90, 5, 0.35);
    border-bottom: 2px solid rgba(170, 255, 140, 0.7);
  }
  .back-contact {
    position: absolute; left: 0; right: 0; top: 368px;
    text-align: center;
    font-family: "Arimo", sans-serif; color: var(--ink-light);
    font-size: 31px; line-height: 39px;
  }
</style>
</head>
<body>
<main class="sheet">
  <section class="card-front">
    <div class="brand">
      <div class="brand-dot"></div>
      <div class="brand-name">QUILLBROOK FUNDS</div>
    </div>
    <div class="holder">
      <div class="holder-name">BARTHOLOMEW ELLING</div>
      <div class="holder-title">Managing Partner</div>
    </div>
    <div class="rule-grey"></div>
    <div class="contact-band">
      <div class="contact-left">
        <div>817 FERN ST SAN FRANCISCO, CA 94111</div>
        <div>415.555.0142 O</div>
        <div>415.555.0187 F</div>
        <div>415.555.0236 C</div>
      </div>
      <div class="contact-right">
        <div>bart@quillbrookfunds.example</div>
        <div>www.quillbrookfunds.example</div>
      </div>
    </div>
  </section>

  <section class="card-back">
    <div class="back-pattern" role="img" aria-label="Green background pattern of overlapping concentric circles"></div>
    <div class="back-brand">
      <div class="brand-dot"></div>
      <div class="brand-name">QUILLBROOK FUNDS</div>
    </div>
    <div class="back-band"></div>
    <div class="back-contact">
      <div>bart@quillbrookfunds.example</div>
      <div>www.quillbrookfunds.example</div>
    </div>
  </section>
</main>
</body>
</html>
```